International Business Development Firm, in need of Branded Stationery material

We just made our Logo and now we are looking for branded stationery for our company such as:

* A Letterhead with our company's name, address, and logo at the top in Word format for easy editing
* A more formal letter format with a light background design (watermark) featuring our logo, allowing us to write over it for various documents and presentations
* Business card + Envelopes are a plus but not a must
* PowerPoint for company and product introductions
* An Info sheet with Bullet Points

The design should be professional.
Please ensure the design is high quality and print ready.

Target Market(s)

Businesses and high net value individuels

Industry/Entity Type

International Business Development Firm

Colors

Designer to choose colors to be used in the design.

Requirements
Must have
• word docs so i can use the stationery templates afterwards

```html
<!DOCTYPE html>
<html lang="en">
<head>
<meta charset="utf-8">
<title>Northvale Capital Stationery</title>
<link href="https://fonts.googleapis.com/css2?family=Open+Sans:wght@400;600;700&family=Arimo:wght@400&family=Orbitron:wght@900&display=swap" rel="stylesheet">
<style>
:root{
  --purple:#6a3c93;
  --purple-dark:#5a3080;
  --board:#868686;
  --paper:#f6f5f5;
  --white:#ffffff;
  --ink:#555;
  --muted:#8a8a8a;
  --rule:#c9c3cf;
  --photo:#4a4a4a;
  --grey-slice:#8c8c8c;
}
*{box-sizing:border-box;margin:0;padding:0}
html,body{width:1200px;height:472px;overflow:hidden;background:var(--board)}
body{position:relative;font-family:"Open Sans",sans-serif;color:var(--ink)}
.sheet{position:absolute;background:var(--white);box-shadow:1px 1px 3px rgba(0,0,0,.35);overflow:hidden}
.brand{font-family:"Open Sans",sans-serif;font-weight:700;color:var(--purple);white-space:nowrap;letter-spacing:.02em}
.brand-dot{display:inline-block;border-radius:50%;background:var(--purple);vertical-align:middle}
.abs{position:absolute}

/* business card */
.card-front{left:20px;top:132px;width:192px;height:110px}
.card-front .brand{position:absolute;left:25px;top:51px;font-size:6.4px;letter-spacing:0}
.card-front .brand-dot{width:6px;height:6px;margin-right:2px;vertical-align:-0.5px}
.card-front .divider{position:absolute;left:109px;top:24px;width:1px;height:62px;background:#ccc}
.card-front .details{position:absolute;left:118px;top:27px;font-size:4px;line-height:5.8px;color:#555}
.card-front .name{font-size:6px;font-weight:700;color:var(--purple);line-height:7px}
.card-front .role{color:var(--muted);margin-bottom:2px}
.card-back{left:19px;top:271px;width:194px;height:110px;background:var(--purple)}
.card-back .brand{position:absolute;left:0;right:0;top:47px;text-align:center;font-size:13px;color:var(--white)}

/* letterhead */
.letter{left:229px;top:41px;width:284px;height:399px;background:var(--paper);font-family:"Arimo",sans-serif}
.letter .brand{position:absolute;left:17px;top:22px;font-size:13px;font-family:"Open Sans",sans-serif}
.letter .brand-dot{width:10px;height:10px;margin-right:4px}
.letter .contact{position:absolute;left:221px;top:11px;font-size:4px;line-height:6px;font-family:"Open Sans",sans-serif;color:#555}
.letter .greeting{position:absolute;left:29px;top:102px;font-size:7.8px;color:#555}
.letter .body{position:absolute;left:29px;top:125px;width:229px;font-size:4.6px;line-height:6.85px;color:#666;text-align:justify}
.letter .body p{margin-bottom:6.7px}
.letter .closing{position:absolute;left:29px;top:275px;font-size:4.6px;color:#666}
.letter .signature{position:absolute;left:28px;top:285px;width:37px;height:14px;background:linear-gradient(90deg,#e8e6e8,#d9d6da)}
.letter .signer{position:absolute;left:30px;top:307px;font-size:6.6px;color:#555}
.letter .signer-role{position:absolute;left:30px;top:317px;font-size:5px;color:#555}
.letter .foot{position:absolute;left:0;right:0;top:386px;text-align:center;font-size:6px;color:#555}

/* slides */
.slide{width:161px;height:121px}
.slide .heading{position:absolute;left:9px;top:11px;font-size:6.6px;color:var(--purple);letter-spacing:.02em}
.slide .sub{position:absolute;left:9px;top:19px;font-size:3.9px;color:var(--muted)}
.slide .rule{position:absolute;left:9px;top:24px;width:136px;height:.5px;background:var(--rule)}
.slide .corner{position:absolute;right:6px;top:12px;font-size:3.6px}
.slide .url{position:absolute;left:0;right:0;bottom:5px;text-align:center;font-size:3.3px;color:var(--purple)}
.tiny{font-size:2.3px;line-height:3.1px;color:#666;text-align:justify}
.label{font-size:3.8px;color:var(--purple)}

.s-title{left:539px;top:47px}
.s-title .brand{position:absolute;left:30px;top:25px;font-size:14px}
.s-title .brand-dot{width:10px;height:10px;margin-right:4px}
.s-title .intro{position:absolute;left:0;right:0;top:69px;text-align:center;font-size:10.3px;line-height:11.3px;color:#777;letter-spacing:.02em}
.s-title .intro b{color:var(--purple);font-weight:600}

.s-team{left:713px;top:47px}
.photo{position:absolute;top:34px;width:31px;height:33px;background:var(--photo);box-shadow:0 0 0 1px #ddd;color:#ddd;font-size:4px;display:flex;align-items:center;justify-content:center}
.member{position:absolute;top:76px;width:32px}
.member .title{font-size:3.2px;color:var(--muted);margin-bottom:3px}

.s-groups{left:539px;top:179px}
.group{position:absolute;width:70px}
.group .label{margin-bottom:1px}

.s-chart{left:713px;top:179px}
.s-pie{left:539px;top:312px}

.s-thanks{left:713px;top:312px;background:var(--purple)}
.s-thanks .big{position:absolute;left:0;right:0;top:40px;text-align:center;font-family:"Orbitron",sans-serif;font-weight:900;font-size:15px;color:var(--white);letter-spacing:.03em}
.s-thanks .small{position:absolute;left:0;right:0;top:58px;text-align:center;font-family:"Orbitron",sans-serif;font-weight:900;font-size:8px;color:var(--white);letter-spacing:.05em}
.s-thanks .info{position:absolute;left:0;right:0;top:100px;text-align:center;font-size:3px;line-height:5px;color:var(--white)}

/* envelopes */
.env-back{left:898px;top:95px;width:262px;height:119px;background:#f4f3f4}
.env-back .brand{position:absolute;left:0;right:0;top:18px;text-align:center;font-size:9px;color:var(--white)}
.env-front{left:896px;top:266px;width:263px;height:120px;background:#f7f6f6}
.env-front .brand{position:absolute;left:12px;top:20px;font-size:10px}
.env-front .brand-dot{width:8px;height:8px;margin-right:3px}
.env-front .addr{position:absolute;left:28px;top:42px;font-size:5px;line-height:7px;color:#666}
</style>
</head>
<body>

<section class="sheet card-front">
  <div class="brand"><span class="brand-dot"></span>NORTHVALE CAPITAL</div>
  <div class="divider"></div>
  <div class="details">
    <div class="name">Laura Bennett</div>
    <div class="role">President</div>
    <div>2170 Harbor Lane</div>
    <div>Glenwood, NY 11020</div>
    <div>&#9742; (555) 0142-7781</div>
    <div>&#9647; (555) 0187-3346</div>
    <div>&#9113; (555) 0163-9025</div>
    <div>&#9993; hello@northvalecap.com</div>
    <div>&#9679; www.northvalecap.com</div>
  </div>
</section>

<section class="sheet card-back">
  <div class="brand">NORTHVALE CAPITAL</div>
</section>

<section class="sheet letter">
  <div class="brand"><span class="brand-dot"></span>NORTHVALE CAPITAL</div>
  <div class="contact">
    2170 Harbor Lane<br>Glenwood, NY 11020<br>
    <span style="display:block;margin-top:3px">&#9742; (555) 0142-7781</span>
    &#9647; (555) 0187-3346<br>
    &#9113; (555) 0163-9025<br>
    &#9993; hello@northvalecap.com
  </div>
  <div class="greeting">Dear Mr. Carter,</div>
  <div class="body">
    <p>Lorem ipsum dolor sit amet, consectetur adipiscing elit. Donec orci purus, luctus vitae dignissim eu, iaculis sed purus. Vivamus faucibus, ipsum nec aliquet viverra, leo mauris condimentum ligula, sit amet sagittis enim ligula quis arcu. Nam egestas tortor id nisi porttitor mattis. In tortor ante, ultricies in suscipit a, tempus non massa. Vivamus et auctor mi. Fusce vel massa nulla. Phasellus nec eros mauris, et scelerisque orci.</p>
    <p>Donec malesuada orci vitae nulla accumsan porta a id massa. Quisque accumsan iaculis magna sit amet fringilla. Maecenas consequat, magna eget tincidunt semper, odio nibh rutrum mi, id feugiat ante nisi eu risus. Vestibulum nunc orci, rhoncus a placerat in, ultricies in mi. Cras mattis varius eros, vel fringilla nisi suscipit eget. Quisque scelerisque sagittis nulla at porttitor.</p>
    <p>Sed id augue vitae urna euismod commodo aliquet a quam. Pellentesque arcu velit, cursus et malesuada ut, consequat et diam. Nullam erat sem, rhoncus id ullamcorper vitae, rhoncus et arcu. In ultricies ultricies nulla, ut rutrum nisi iaculis at. Donec eu magna a metus ornare faucibus. Fusce aliquet faucibus ultricies. Morbi semper, est id tincidunt gravida, sem arcu adipiscing lacus, ac bibendum nulla leo eu purus. Quisque nec diam sed risus consectetur a cumsan quis quis nibh. Vestibulum id purus lorem.</p>
    <p>It is a long established fact that a reader will be distracted by the readable content of a page when looking at its layout. The point of using Lorem Ipsum is that it has a more-or-less normal distribution of letters, as opposed to using 'Content here, content here', making it look like readable English. Many desktop publishing packages</p>
  </div>
  <div class="closing">Sincerely,</div>
  <div class="signature" role="img" aria-label="Handwritten signature"></div>
  <div class="signer">Mark Ellison</div>
  <div class="signer-role">CEO/ Founder</div>
  <div class="foot">www.northvalecap.com</div>
</section>

<section class="sheet slide s-title">
  <div class="brand"><span class="brand-dot"></span>NORTHVALE</div>
  <div class="intro">WELCOME TO OUR<br><b>PRESENTATION NAME</b><br>DESCRIPTION</div>
</section>

<section class="sheet slide s-team">
  <div class="heading">HEADING HERE</div><div class="sub">Sub Heading</div><div class="rule"></div>
  <div class="corner brand">NV</div>
  <div class="photo" style="left:12px">Photo</div>
  <div class="photo" style="left:48px">Photo</div>
  <div class="photo" style="left:84px">Photo</div>
  <div class="photo" style="left:117px">Photo</div>
  <div class="member" style="left:13px"><div class="label">Team member1</div><div class="title">Title</div><div class="tiny">Short note on role and focus.</div></div>
  <div class="member" style="left:49px"><div class="label">Team member2</div><div class="title">Title</div><div class="tiny">Short note on role and focus.</div></div>
  <div class="member" style="left:85px"><div class="label">Team member3</div><div class="title">Title</div><div class="tiny">Short note on role and focus.</div></div>
  <div class="member" style="left:119px"><div class="label">Team member4</div><div class="title">Title</div><div class="tiny">Short note on role and focus.</div></div>
  <div class="url">www.northvalecap.com</div>
</section>

<section class="sheet slide s-groups">
  <div class="heading">HEADING HERE</div><div class="sub">Sub Heading</div><div class="rule"></div>
  <div class="corner brand">NV</div>
  <div class="group" style="left:9px;top:31px"><div class="label">Group1</div><div class="tiny">Brief summary of this group and its core services.</div></div>
  <div class="group" style="left:82px;top:31px"><div class="label">Group4</div><div class="tiny">Brief summary of this group and its core services.</div></div>
  <div class="group" style="left:9px;top:56px"><div class="label">Group2</div><div class="tiny">Brief summary of this group and its core services.</div></div>
  <div class="group" style="left:82px;top:56px"><div class="label">Group5</div><div class="tiny">Brief summary of this group and its core services.</div></div>
  <div class="group" style="left:9px;top:80px"><div class="label">Group3</div><div class="tiny">Brief summary of this group and its core services.</div></div>
  <div class="group" style="left:82px;top:80px"><div class="label">Group6</div><div class="tiny">Brief summary of this group and its core services.</div></div>
  <div class="url">www.northvalecap.com</div>
</section>

<section class="sheet slide s-chart">
  <div class="heading">HEADING HERE</div><div class="sub">Sub Heading</div><div class="rule"></div>
  <div class="corner brand">NV</div>
  <svg class="abs" style="left:14px;top:31px" width="66" height="50" viewBox="0 0 66 50">
    <g stroke="#d8d8d8" stroke-width=".4">
      <line x1="0" y1="2" x2="66" y2="2"/><line x1="0" y1="8" x2="66" y2="8"/><line x1="0" y1="14" x2="66" y2="14"/>
      <line x1="0" y1="20" x2="66" y2="20"/><line x1="0" y1="26" x2="66" y2="26"/><line x1="0" y1="32" x2="66" y2="32"/>
      <line x1="0" y1="38" x2="66" y2="38"/><line x1="0" y1="44" x2="66" y2="44"/><line x1="0" y1="49" x2="66" y2="49"/>
    </g>
    <g fill="var(--purple)">
      <rect x="16" y="2" width="8" height="47"/><rect x="26" y="8" width="8" height="41"/>
      <rect x="36" y="19" width="8" height="30"/><rect x="46" y="11" width="8" height="38"/>
    </g>
    <g fill="#fff" font-size="2.4" font-family="Open Sans, sans-serif">
      <text transform="translate(21.5 47) rotate(-90)">Sub text1</text>
      <text transform="translate(31.5 47) rotate(-90)">Sub text2</text>
      <text transform="translate(41.5 47) rotate(-90)">Sub text3</text>
      <text transform="translate(51.5 47) rotate(-90)">Sub text4</text>
    </g>
  </svg>
  <div class="abs tiny" style="left:97px;top:31px;width:44px">Key figures for the year at a glance.</div>
  <div class="abs tiny" style="left:97px;top:55px;width:44px">Key figures for the year at a glance.</div>
  <div class="abs tiny" style="left:13px;top:88px;width:135px">Results grew steadily across all four regions this year, led by strong client demand.</div>
  <div class="url">www.northvalecap.com</div>
</section>

<section class="sheet slide s-pie">
  <div class="heading">HEADING HERE</div><div class="sub">Sub Heading</div><div class="rule"></div>
  <div class="corner brand">NV</div>
  <div class="abs tiny" style="left:12px;top:39px;width:70px;text-align:center">Overview of how our portfolio is split between sectors and regions over the period.</div>
  <div class="abs tiny" style="left:12px;top:85px;width:70px;text-align:center">Overview of how our portfolio is split between sectors and regions over the period.</div>
  <svg class="abs" style="left:100px;top:34px" width="38" height="38" viewBox="-19 -19 38 38">
    <circle r="18" fill="var(--purple)"/>
    <path d="M0 0 L0 -18 A18 18 0 0 1 15.6 -9 Z" fill="var(--grey-slice)"/>
    <path d="M0 0 L17.7 3 A18 18 0 0 1 6 17 Z" fill="var(--grey-slice)"/>
  </svg>
  <div class="abs" style="left:99px;top:78px;width:44px;font-size:2.4px;line-height:5px;color:#555">
    <div style="border-bottom:.4px solid #ccc"><span style="display:inline-block;width:3px;height:3px;background:var(--purple);margin-right:3px"></span>Sector one 50%</div>
    <div style="border-bottom:.4px solid #ccc"><span style="display:inline-block;width:3px;height:3px;background:var(--grey-slice);margin-right:3px"></span>Sector two 50%</div>
    <div class="tiny" style="margin-top:4px">Figures are rounded.</div>
  </div>
  <div class="url">www.northvalecap.com</div>
</section>

<section class="sheet slide s-thanks">
  <div class="big">THANKS</div>
  <div class="small">FOR COMING</div>
  <div class="info">2170 Harbor Lane, Glenwood, NY 11020<br>&#9742; (555) 0142-7781 &nbsp;&#9647; (555) 0187-3346 &nbsp;&#9113; (555) 0163-9025<br>&#9993; hello@northvalecap.com &nbsp;&#9679; www.northvalecap.com</div>
</section>

<section class="sheet env-back">
  <svg class="abs" style="left:0;top:0" width="262" height="45" viewBox="0 0 262 45">
    <path d="M0 0 H262 L260 8 Q258 44 236 44 H26 Q6 44 4 8 Z" fill="var(--purple)"/>
  </svg>
  <div class="brand">NORTHVALE</div>
</section>

<section class="sheet env-front">
  <div class="brand"><span class="brand-dot"></span>NORTHVALE CAPITAL</div>
  <div class="addr">2170 Harbor Lane<br>Glenwood, NY 11020</div>
</section>

</body>
</html>
```